Cork Meadow Excursions Post Card/Flyer

Postcard/flyer needs to convey our mission: to provide an authentic, boutique wine tour of exceptional quality with first class customer service. It needs to be clean and high quality. Less is more :) Worthy of 5 star hotel concierges handing them to a guest. I provided an old flyer my friend made and my competitors flyer. Please use these just as reference, but i want to see your creativity. I like the format of "Gentle Harvest" -scan 91-flyer BUT I don't want to copy.

Target Market(s)

Couples, travelers, hotel employees, local industry, etc...

Industry/Entity Type

Boutique

Requirements
Must have
• Must have bullet points of the my previous reference flyer and any photos .Please use website for reference too.
• Yelp, trip advisor affirmations Plus Instagram
• "Group and Private Tours available"
• "Mention this card for 10% off any tour" - low key please
• corkmeadowexcursions.com, info@corkmeadowexcursions.com, 805-219-6384
Nice to have
• clean lines , simple and elegant
• double sided please
Should not have
• Not too busy.

```html
<!DOCTYPE html>
<html lang="en">
<head>
<meta charset="utf-8">
<title>Cork Meadow Excursions – Flyer</title>
<link href="https://fonts.googleapis.com/css2?family=Oswald:wght@500;600&family=Questrial&family=Open+Sans:wght@400&display=swap" rel="stylesheet">
<style>
  :root{
    --green-dark:#0f5a33;
    --green-tint:rgba(20,120,65,.82);
    --green-bright:rgba(35,190,100,.82);
    --mint:#c6ebd5;
    --mint-soft:#e3f6ea;
    --white:#ffffff;
    --page:#d6d7d6;
  }
  *{box-sizing:border-box;margin:0;padding:0}
  html,body{width:1200px;height:1200px;overflow:hidden}
  body{background:linear-gradient(90deg,#e6e6e6,var(--page) 50%,#e6e6e6);position:relative;font-family:"Questrial",sans-serif}
  .side{position:absolute;top:0;height:1200px;overflow:hidden}
  .front{left:16px;width:564px;background:var(--white)}
  .back{left:616px;width:566px;background:var(--green-dark)}

  /* front */
  .brand-box{position:absolute;left:0;top:0;width:190px;height:134px;border:1px solid #e4e4e4;background:#fff;display:flex;align-items:center;justify-content:center;gap:8px}
  .brand-mark{width:12px;height:12px;background:var(--green-dark);flex:none}
  .brand-name{font-family:"Oswald",sans-serif;font-weight:500;color:var(--green-dark);font-size:17px;line-height:1.15;text-transform:uppercase;letter-spacing:1px}
  .front-title{position:absolute;left:192px;right:0;top:20px;text-align:center;font-family:"Oswald",sans-serif;font-weight:600;color:var(--green-dark);text-transform:uppercase;line-height:1;white-space:nowrap}
  .front-title .name{font-size:31px;letter-spacing:-.4px}
  .front-title .place{font-size:30px;margin-top:12px}
  .hero-photo{position:absolute;left:0;top:400px;width:564px;height:752px;
    background:linear-gradient(180deg,#b9d3ea 0%,#dfe9f0 18%,#8f8b6a 26%,#5e7a45 38%,#4d7a38 55%,#6f8f45 75%,#5a4a35 100%)}
  .angles{position:absolute;left:0;top:0;width:564px;height:520px}
  .headline{position:absolute;left:30px;top:312px;transform:rotate(-9.5deg);transform-origin:left top;font-family:"Oswald",sans-serif;font-weight:600;color:#fff;font-size:45px;line-height:1.45;text-transform:uppercase;letter-spacing:-.3px;white-space:nowrap}
  .tag{position:absolute;background:var(--green-tint);color:#fff;font-size:32px;padding:0 8px;white-space:nowrap}
  .explore-1{left:0;top:520px;width:340px;height:48px;line-height:48px}
  .explore-2{left:0;top:568px;width:364px;height:48px;line-height:48px}
  .explore-3{left:0;top:616px;width:175px;height:40px;line-height:40px;background:var(--green-bright)}
  .offer-1{right:4px;top:774px;text-align:right;font-size:36px;height:48px;line-height:48px;padding:0 4px 0 6px}
  .offer-2{right:4px;top:822px;text-align:right;font-size:36px;height:46px;line-height:46px;padding:0 4px 0 12px}
  .front-footer{position:absolute;left:0;bottom:0;width:564px;height:48px;background:var(--green-dark);color:#fff;display:flex;align-items:center;justify-content:center;gap:11px;font-size:14px;white-space:nowrap}
  .front-footer .sep{width:2px;height:24px;background:#fff}

  /* back */
  .couple-photo{position:absolute;left:0;top:0;width:566px;height:200px;background:linear-gradient(135deg,#8aa55c,#c9c8a0 55%,#7d8f4c)}
  .box-title{position:absolute;background:#fff;color:var(--green-dark);font-family:"Oswald",sans-serif;font-weight:500;text-transform:uppercase;text-align:center;white-space:nowrap}
  .signup{left:14px;top:218px;width:532px;height:38px;font-size:21.5px;line-height:38px;letter-spacing:-.4px}
  .perks{position:absolute;left:26px;top:262px;list-style:none;font-family:"Open Sans",sans-serif;color:#fff;font-size:21px;line-height:29px}
  .perks li{display:flex;align-items:center;gap:10px}
  .perks li::before{content:"";width:11px;height:11px;background:#fff;flex:none}
  .divider{position:absolute;left:15px;top:390px;width:536px;height:1px;background:#d5e6db}
  .rated{left:40px;top:410px;width:482px;height:36px;font-size:29px;line-height:36px;letter-spacing:-.4px}
  .review-badge{position:absolute;left:217px;top:458px;width:153px;height:108px;background:#fff;border:2px solid #fff}
  .review-badge span{position:absolute;left:0;right:0;bottom:0;height:26px;background:#c8102e}
  .group-tours{position:absolute;left:0;width:566px;top:578px;text-align:center;font-family:"Oswald",sans-serif;font-weight:500;color:#fff;font-size:20px;text-transform:uppercase;letter-spacing:-.2px}
  .gallery-photo{position:absolute;width:268px;height:204px}
  .g-1{left:10px;top:621px;background:linear-gradient(180deg,#cfd6c8,#7f8e55 45%,#b08a3c 75%,#6b4a2a)}
  .g-2{left:286px;top:621px;background:linear-gradient(135deg,#c4d2be,#5f8c3a 50%,#d8b38a)}
  .g-3{left:10px;top:835px;background:linear-gradient(180deg,#8d9a78,#5d7e3c 45%,#d9d5c5 75%,#6f7a4e)}
  .g-4{left:286px;top:835px;background:linear-gradient(180deg,#e0e3e6,#c8ccc9 30%,#7ea452 60%,#9c8a6a)}
  .contact-bar{position:absolute;left:0;top:1056px;width:566px;height:144px;background:#fff}
  .contact-brand{position:absolute;left:10px;top:6px;width:186px;height:132px;border:1px solid #e4e4e4;display:flex;align-items:center;justify-content:center;gap:8px}
  .contact-title{position:absolute;left:202px;right:6px;top:14px;text-align:center;font-family:"Oswald",sans-serif;font-weight:600;color:var(--green-dark);font-size:27px;line-height:1;text-transform:uppercase;letter-spacing:-.5px;white-space:nowrap}
  .contact-list{position:absolute;left:236px;top:58px;list-style:none;color:var(--green-dark);font-family:"Questrial",sans-serif;font-size:17px;white-space:nowrap}
  .contact-list li{display:flex;align-items:center;gap:8px;height:26px}
  .contact-list svg{width:20px;height:20px;flex:none}
</style>
</head>
<body>

<section class="side front">
  <div class="brand-box">
    <span class="brand-mark"></span>
    <span class="brand-name">Cork Meadow<br>Excursions</span>
  </div>
  <div class="front-title">
    <div class="name">CORK MEADOW EXCURSIONS</div>
    <div class="place">Santa Barbara</div>
  </div>

  <div class="hero-photo" role="img" aria-label="Photo of vineyard rows leading toward green hills under a blue sky"></div>

  <svg class="angles" viewBox="0 0 564 520" aria-hidden="true">
    <polygon points="0,144 400,205 564,100 564,200 0,294" fill="var(--mint-soft)"/>
    <polygon points="0,144 330,240 0,294" fill="var(--mint)"/>
    <polygon points="0,294 564,200 564,384 0,480" fill="var(--green-dark)"/>
    <polygon points="0,480 564,384 564,410 0,496" fill="var(--mint-soft)" opacity=".8"/>
  </svg>
  <div class="headline">An authentic and boutique<br>wine tour experience</div>

  <div class="tag explore-1">Come Explore Santa</div>
  <div class="tag explore-2">Barbara Wine Country</div>
  <div class="tag explore-3">with us!</div>

  <div class="tag offer-1">Mention this card for 10%</div>
  <div class="tag offer-2">off any tour</div>

  <footer class="front-footer">
    <span>corkmeadowexcursions.com</span><span class="sep"></span>
    <span>info@corkmeadowexcursions.com</span><span class="sep"></span>
    <span>805-219-6384</span>
  </footer>
</section>

<section class="side back">
  <div class="couple-photo" role="img" aria-label="Photo of a couple pouring white wine in a vineyard"></div>

  <div class="box-title signup">Sign up for our all inclusive wine tour and experience</div>
  <ul class="perks">
    <li>Premium wine tasting at boutique wineries</li>
    <li>Safe and comfortable luxury vehicles</li>
    <li>Picnic lunch in a vineyard setting</li>
    <li>Local expert Guides</li>
  </ul>
  <div class="divider"></div>

  <div class="box-title rated">A top rated and top ranked company</div>
  <div class="review-badge" role="img" aria-label="Five star review listing badge"><span></span></div>
  <div class="group-tours">Group and private tours available</div>

  <div class="gallery-photo g-1" role="img" aria-label="Photo of a wine bottle, glasses, grapes and cheese overlooking hills"></div>
  <div class="gallery-photo g-2" role="img" aria-label="Photo of a guide pouring wine for guests among the vines"></div>
  <div class="gallery-photo g-3" role="img" aria-label="Photo of a tour group walking through a vineyard"></div>
  <div class="gallery-photo g-4" role="img" aria-label="Photo of friends jumping for joy in a vineyard"></div>

  <div class="contact-bar">
    <div class="contact-brand">
      <span class="brand-mark"></span>
      <span class="brand-name">Cork Meadow<br>Excursions</span>
    </div>
    <div class="contact-title">Contact us for availability</div>
    <ul class="contact-list">
      <li>
        <svg viewBox="0 0 20 20" aria-hidden="true"><rect x="1" y="1" width="18" height="18" rx="3" fill="var(--green-dark)"/><path d="M7 5c-1 0-2 1-1.6 2.6.8 3 3.2 5.6 6.4 6.8 1.4.5 2.4-.4 2.6-1.4l-2-1.4-1.2 1c-1.6-.8-2.8-2-3.4-3.6l1-1.2L7.4 5z" fill="#fff"/></svg>
        805-219-6384
      </li>
      <li>
        <svg viewBox="0 0 20 20" aria-hidden="true"><rect x="1.5" y="4" width="17" height="12" fill="none" stroke="var(--green-dark)" stroke-width="1.4"/><path d="M1.5 4l8.5 7 8.5-7" fill="none" stroke="var(--green-dark)" stroke-width="1.4"/></svg>
        info@corkmeadowexcursions.com
      </li>
      <li>
        <svg viewBox="0 0 20 20" aria-hidden="true"><g fill="none" stroke="var(--green-dark)" stroke-width="1.3"><circle cx="10" cy="10" r="8.5"/><ellipse cx="10" cy="10" rx="3.8" ry="8.5"/><path d="M1.5 10h17M3 5.5h14M3 14.5h14"/></g></svg>
        corkmeadowexcursions.com
      </li>
    </ul>
  </div>
</section>

</body>
</html>
```